Church Grand Opening Bill Board design

I would like to create a bill board design for our church's grand opening. I would like to incorporate pictures of two separate preachers with a creative way of blending them both together so it won't take up too much space. I have included pictures and logo.

I am open for color coordination and I have included a couple of past designs to use as a reference

The information I would want on the Build Board is the following (1) Grand Opening (2) 4218 E. Marlowe Avenue (3) 10:30am (4) Multi-Ethnic Church Planting Church (5) Sept. 26, 2021

Target Market(s)

Church shoppers and those who have never been connected to a church

Font styles to use
Serif

Requirements
Must have
• Our Logo
Nice to have
• i do not want any crosses or religious symbols

```html
<!DOCTYPE html>
<html lang="en">
<head>
<meta charset="utf-8">
<title>Kindle Church – Grand Opening Billboard</title>
<link rel="stylesheet" href="https://fonts.googleapis.com/css2?family=Archivo+Black&family=Source+Serif+4:wght@600;700&display=swap">
<style>
  :root {
    --page: #b9b9b9;
    --sky-top: #5f9fd6;
    --sky-mid: #c9dcec;
    --haze: #e6ecf1;
    --paving: #d3d7db;
    --paving-dark: #b5bbc1;
    --orange: #f4922a;
    --ink: #160c0d;
    --photo-left-a: #4a4f57;
    --photo-left-b: #1b1d22;
    --photo-right-a: #5a3b2c;
    --photo-right-b: #231a18;
  }
  * { box-sizing: border-box; margin: 0; padding: 0; }
  html, body { width: 927px; height: 1200px; overflow: hidden; }
  body {
    background: var(--page);
    display: flex;
    align-items: center;
    justify-content: center;
  }
  .billboard {
    position: relative;
    width: 880px;
    height: 410px;
    overflow: hidden;
    background: linear-gradient(180deg, var(--sky-top) 0%, var(--sky-mid) 38%, var(--haze) 62%, var(--paving) 66%, var(--paving-dark) 100%);
    box-shadow: 0 14px 24px rgba(0,0,0,0.35);
  }
  .skyline {
    position: absolute;
    left: 0; right: 0;
    top: 160px;
    height: 112px;
    background: linear-gradient(180deg, rgba(120,140,160,0.15), rgba(110,125,140,0.45));
  }
  .preacher {
    position: absolute;
    bottom: 0;
  }
  .preacher--left {
    left: 0;
    width: 287px;
    height: 375px;
    background: linear-gradient(180deg, var(--photo-left-a), var(--photo-left-b));
    clip-path: polygon(28% 0, 60% 0, 70% 30%, 100% 40%, 100% 100%, 0 100%, 0 45%, 30% 32%);
  }
  .preacher--right {
    left: 605px;
    width: 275px;
    height: 358px;
    background: linear-gradient(180deg, var(--photo-right-a), var(--photo-right-b));
    clip-path: polygon(30% 0, 62% 0, 68% 30%, 100% 40%, 100% 100%, 0 100%, 5% 42%, 30% 30%);
  }
  .content {
    position: absolute;
    left: 300px;
    width: 306px;
    top: 0;
    height: 100%;
    text-align: center;
    color: var(--ink);
  }
  .brand {
    position: absolute;
    top: 58px;
    left: 0; right: 0;
    display: flex;
    align-items: center;
    justify-content: center;
    gap: 10px;
  }
  .brand__dot {
    width: 30px; height: 30px;
    border-radius: 50%;
    background: var(--orange);
  }
  .brand__name {
    font-family: "Source Serif 4", serif;
    font-weight: 700;
    font-size: 34px;
    color: var(--ink);
  }
  .headline {
    position: absolute;
    top: 150px;
    left: 0; right: 0;
    font-family: "Archivo Black", sans-serif;
    font-size: 58px;
    line-height: 58px;
  }
  .headline__grand { color: var(--orange); display: block; }
  .headline__opening { color: var(--ink); display: block; }
  .tagline {
    position: absolute;
    top: 274px;
    left: 13px;
    width: 285px;
    height: 25px;
    line-height: 25px;
    background: var(--orange);
    border-radius: 2px;
    font-family: "Source Serif 4", serif;
    font-weight: 700;
    font-size: 13px;
    color: var(--ink);
  }
  .details {
    position: absolute;
    top: 326px;
    left: 0; right: 0;
    display: flex;
    justify-content: center;
    align-items: center;
    gap: 6px;
    font-family: "Archivo Black", sans-serif;
    font-size: 16px;
  }
  .details__divider {
    width: 1px; height: 18px;
    background: var(--orange);
  }
  .details svg { width: 14px; height: 14px; }
  .address {
    position: absolute;
    top: 354px;
    left: 0; right: 0;
    display: flex;
    justify-content: center;
    align-items: center;
    gap: 6px;
    font-family: "Source Serif 4", serif;
    font-weight: 600;
    font-size: 15px;
  }
  .address svg { width: 16px; height: 16px; }
</style>
</head>
<body>
  <section class="billboard">
    <div class="skyline" role="img" aria-label="City skyline with glass towers on a rooftop terrace"></div>

    <div class="preacher preacher--left" role="img" aria-label="Photo of the first preacher in a dark jacket, speaking with a headset microphone"></div>
    <div class="preacher preacher--right" role="img" aria-label="Photo of the second preacher in a dark polo shirt, smiling"></div>

    <div class="content">
      <div class="brand">
        <span class="brand__dot"></span>
        <span class="brand__name">Kindle Church</span>
      </div>

      <h1 class="headline">
        <span class="headline__grand">GRAND</span>
        <span class="headline__opening">OPENING</span>
      </h1>

      <p class="tagline">Multi-Ethnic Church Planting Church</p>

      <p class="details">
        <svg viewBox="0 0 16 16" aria-hidden="true"><rect x="1.5" y="2.5" width="13" height="12" rx="1.5" fill="none" stroke="#160c0d" stroke-width="1.2"/><line x1="1.5" y1="6" x2="14.5" y2="6" stroke="#160c0d" stroke-width="1.2"/><line x1="5" y1="1" x2="5" y2="4" stroke="#160c0d" stroke-width="1.2"/><line x1="11" y1="1" x2="11" y2="4" stroke="#160c0d" stroke-width="1.2"/></svg>
        <span>Sept. 26 , 2021</span>
        <span class="details__divider"></span>
        <svg viewBox="0 0 16 16" aria-hidden="true"><circle cx="8" cy="8" r="6.5" fill="none" stroke="#160c0d" stroke-width="1.4"/><path d="M8 4v4l2.5 1.5" fill="none" stroke="#160c0d" stroke-width="1.4"/></svg>
        <span>10:30am</span>
      </p>

      <p class="address">
        <svg viewBox="0 0 16 16" aria-hidden="true"><circle cx="8" cy="8" r="7" fill="none" stroke="#160c0d" stroke-width="1"/><path d="M8 3.2a3 3 0 0 0-3 3c0 2.3 3 6 3 6s3-3.7 3-6a3 3 0 0 0-3-3z" fill="#f4922a"/><circle cx="8" cy="6.2" r="1.1" fill="#fff"/></svg>
        <span>4218 E. Marlowe Avenue</span>
      </p>
    </div>
  </section>
</body>
</html>
```